Business Card Design

Consultation for design, construction athletic facilities specializing in synthetic turf systems and all weather running track systems.
Motto "True Owner Representation"
New Company that we'd like to highlight the LOGO first and foremost with the colors of the background and font as primary colors of the card too if possible. I've also attached a typical larger project design layout that could be used in the background to highlight our design and construction specialty.
Website is something we want very noticeable for driving traffic.
Target Market(s)
Athletic Directors, Designers, Government and Military, Contractors
Industry/Entity Type
Construction
Contact Information for Business Card
Peter L. Vandrell CFB, CTB
48317 W 63rd Ave
Harlow Ridge, WA 99482
C +1 503.555.0147
O +1 808.555.0182
Peter@fieldlaneco.example
www.fieldlaneco.example

```html
<!DOCTYPE html>
<html lang="en">
<head>
<meta charset="utf-8">
<title>Halvern Sport – Business Card</title>
<link rel="stylesheet" href="https://fonts.googleapis.com/css2?family=Carlito:wght@400;700&display=swap">
<style>
  :root {
    --stage: #b9b9b9;
    --card: #050505;
    --orange: #f7941d;
    --orange-text: #f08a1c;
    --ink: #111111;
    --drawing-a: #3a1e08;
    --drawing-b: #b8641c;
  }
  * { box-sizing: border-box; margin: 0; padding: 0; }
  html, body {
    width: 1200px; height: 900px; overflow: hidden;
    background: var(--stage);
    font-family: "Carlito", "Calibri", sans-serif;
  }
  .stage { position: relative; width: 1200px; height: 900px; }
  .card {
    position: absolute; top: 295px;
    width: 540px; height: 309px;
    background: var(--card);
    overflow: hidden;
    box-shadow: 0 6px 18px rgba(0,0,0,0.35);
  }
  .card--front { left: 45px; }
  .card--back { left: 615px; }

  .holder { position: absolute; right: 300px; top: 62px; text-align: right; color: var(--orange-text); }
  .holder__name { font-size: 27px; font-weight: 700; letter-spacing: 0.2px; }
  .holder__title { font-size: 14px; margin-top: 6px; }

  .brand { position: absolute; left: 286px; top: 48px; display: flex; align-items: center; gap: 10px; color: var(--orange-text); }
  .brand__dot { width: 22px; height: 22px; border-radius: 50%; background: var(--orange); }
  .brand__name { font-size: 30px; font-weight: 400; letter-spacing: 3px; line-height: 1; }

  .divider { position: absolute; left: 262px; top: 118px; width: 1px; height: 70px; background: linear-gradient(var(--card), var(--orange), var(--card)); }

  .contact { position: absolute; left: 286px; top: 126px; color: var(--orange-text); font-size: 14.5px; line-height: 1.45; }

  .band {
    position: absolute; left: 0; right: 0; bottom: 28px; height: 48px;
    background: var(--orange);
    display: flex; align-items: center; justify-content: space-between;
    padding: 0 46px 0 30px;
    color: var(--ink); font-size: 15px;
  }
  .band__item { display: flex; align-items: center; gap: 7px; }
  .band__web { font-size: 17px; }
  .band svg { width: 15px; height: 15px; }

  .site-plan {
    position: absolute; left: 95px; top: 40px; width: 350px; height: 220px;
    background: radial-gradient(ellipse at center, var(--drawing-b) 0%, var(--drawing-a) 70%, var(--card) 100%);
    opacity: 0.75; border-radius: 90px 110px 110px 90px;
  }
</style>
</head>
<body>
<main class="stage">
  <section class="card card--front" aria-label="Business card front">
    <div class="holder">
      <p class="holder__name">Peter L. Vandrell</p>
      <p class="holder__title">CFB, CTB</p>
    </div>
    <div class="brand">
      <span class="brand__dot"></span>
      <span class="brand__name">HALVERN sport</span>
    </div>
    <span class="divider"></span>
    <div class="contact">
      <p>C +1 503.555.0147</p>
      <p>O +1 808.555.0182</p>
      <p>48317 W 63rd Ave Harlow Ridge,</p>
      <p>WA 99482</p>
    </div>
    <div class="band">
      <span class="band__item">
        <svg viewBox="0 0 16 16" fill="none" stroke="currentColor" stroke-width="1.4"><rect x="1.5" y="3.5" width="13" height="9"/><path d="M1.5 3.5 8 9l6.5-5.5"/></svg>
        Peter@fieldlaneco.example
      </span>
      <span class="band__item band__web">
        <svg viewBox="0 0 16 16" fill="currentColor"><circle cx="8" cy="8" r="7"/><path d="M1 8h14M8 1c-3 3-3 11 0 14M8 1c3 3 3 11 0 14" stroke="var(--orange)" stroke-width="1" fill="none"/></svg>
        www.fieldlaneco.example
      </span>
    </div>
  </section>

  <section class="card card--back" aria-label="Business card back">
    <div class="site-plan" role="img" aria-label="Orange line drawing of an athletic complex site plan with running track and ball fields"></div>
  </section>
</main>
</body>
</html>
```